Flyer Design for Business: "Velvet Dune"

My Business name is "VELVET DUNE"

Laser Hair Removal
Non invasive and pain free
Look amazing and feel confident with a Hair Free body
Now is the time to start don't delay
1 treatment a month will ensure you are bikini hot for the summer months
Take full advantage of our OPENING SPECIALS of 30%-40% savings
Part payments available

CELLULITE & FAT REDUCTION
Now you too can look amazing without invasive surgery, downtime or discomfort
Lorna Pettigrew & Beatrix Holloway are avid recipients of this treatment.
Effective on all skin types and delivers fast measurable results for:
Helping mums regain their pre-baby figures
Losing the love handles (but keeping the love)
Stretch mark reduction
Skin tightening
Cellulite busting on Arms, tummy, thighs.
Man boob reduction.
Latest technology:
Bi Polar radio frequency (RF)
infrared light
negative pressure (Vacuum)
Tissue manipulation through roller mechanical massage.
50% saving Call now

PDT LED REJUVENATION LIGHT THERAPY
KOTR Researchers found:
Fibroblast and muscles grew 5 times faster, stimulates
reconstruction of collagenous fibres of the dermis
These findings and more assist with:
Remove freckles, sunburn pigmentation,
Cures acne and hair follicle inflammation
Anti aging skin tightening
Reduces pore size
Improve the skin texture
Improves circulation
Red light : reduces pore size, softens skin wrinkles,reduces acne
Blue light: Kills the acne bacillus to eliminate acne, inhibit inflammation
Yellow light: Skin tightening, whitening and softens skin wrinkles
Purple light: combination of red & blue lights treats acne scars
Orange light increases cell energy and accelerates metabolism
$55 Saving and relax under the lights.

Who can resist a soothing Hot stone massage therapy after:
A hard stressful day at work
Aches and muscular pain

Pick anything from this info with a couple of nice images.

Target Market(s)

Females & males Sports minded people cyclists

Industry/Entity Type

Beauty Salon

Colors
00a990
e34197

Requirements
Must have
• a couple of images and
Nice to have
• Pink and bluey green like my business card

```html
<!DOCTYPE html>
<html lang="en">
<head>
<meta charset="utf-8">
<title>Velvet Dune — Flyer</title>
<link rel="stylesheet" href="https://fonts.googleapis.com/css2?family=Great+Vibes&family=Oswald:wght@300&family=Roboto+Condensed:wght@300;400;700&family=Roboto:wght@400;700&display=swap">
<style>
  :root{
    --pink:#e34197;
    --teal:#00a990;
    --ink:#3d3d3d;
    --grey:#666;
    --white:#ffffff;
    --hero-tone:#d8eeee;
    --hero-mid:#eef6f3;
  }
  *{box-sizing:border-box;margin:0;padding:0}
  html,body{width:899px;height:1200px;overflow:hidden;background:#fff}
  body{font-family:"Roboto",Arial,sans-serif;color:var(--ink)}
  .flyer{position:relative;width:899px;height:1200px;overflow:hidden;background:var(--white)}

  /* hero */
  .hero-photo{position:absolute;left:0;top:0;width:899px;height:470px;
    background:linear-gradient(90deg,var(--hero-tone) 0%,var(--hero-mid) 42%,#fff 68%,#fff 100%);}
  .brand-title{position:absolute;right:40px;top:40px;font-family:"Great Vibes",cursive;font-size:86px;font-weight:400;color:var(--pink);line-height:1}
  .hero-points{position:absolute;left:481px;top:152px;width:380px;list-style:none;font-size:14px;line-height:19px;color:var(--ink)}
  .hero-points li{position:relative;padding-left:18px;margin-bottom:2px}
  .hero-points li::before{content:"";position:absolute;left:2px;top:7px;width:6px;height:6px;border-radius:50%;background:var(--pink)}
  .hero-curve{position:absolute;left:0;top:330px;width:899px;height:160px}

  .offer-badge{position:absolute;left:640px;top:262px;width:172px;height:172px}
  .offer-badge svg{position:absolute;inset:0}
  .offer-text{position:absolute;inset:0;display:flex;flex-direction:column;align-items:center;justify-content:center;text-align:center;color:#fff;font-family:"Roboto Condensed",Arial,sans-serif;font-weight:700;line-height:1.02;transform:rotate(-4deg)}
  .offer-text .small{font-size:14px}
  .offer-text .big{font-size:28px}

  /* left column */
  .intro{position:absolute;left:40px;top:500px;width:440px}
  .intro-lead{font-family:"Roboto Condensed",Arial,sans-serif;font-weight:300;font-size:33px;line-height:56px;color:var(--grey);white-space:nowrap}
  .intro-lead .script{font-family:"Great Vibes",cursive;font-size:60px;color:var(--teal);vertical-align:-6px}
  .intro-headline{font-family:"Oswald",Impact,sans-serif;font-weight:300;font-size:92px;line-height:96px;color:var(--pink);letter-spacing:-1px}

  .faint-portrait{position:absolute;left:160px;top:790px;width:320px;height:220px;border-radius:50%;
    background:radial-gradient(ellipse at center,rgba(200,200,200,.35) 0%,rgba(220,220,220,.15) 50%,rgba(255,255,255,0) 72%)}

  .cellulite{position:absolute;left:40px;top:668px;width:440px;font-size:13.5px;line-height:18px}
  .section-head{font-family:"Roboto Condensed",Arial,sans-serif;font-weight:700;font-size:15px;color:var(--teal);text-transform:uppercase;margin-bottom:8px}
  .cellulite p{margin-bottom:8px}
  .dot-list{list-style:none;margin-bottom:6px}
  .dot-list li{position:relative;padding-left:18px}
  .dot-list li::before{content:"";position:absolute;left:3px;top:6px;width:6px;height:6px;border-radius:50%;background:var(--teal)}
  .sub-head{font-family:"Roboto Condensed",Arial,sans-serif;font-weight:700;font-size:15px;color:var(--teal);margin:6px 0 4px}
  .call-out{position:absolute;left:150px;top:1004px;font-family:"Roboto Condensed",Arial,sans-serif;font-weight:700;color:var(--pink);font-size:20px}
  .call-out .num{font-size:32px}

  /* light therapy panel */
  .therapy-panel{position:absolute;left:492px;top:478px;width:407px;height:478px;background:var(--pink);border-bottom-left-radius:70px;padding:18px 24px 0 26px;color:#fff;font-size:12.5px;line-height:15.5px}
  .therapy-panel h2{font-family:"Roboto Condensed",Arial,sans-serif;font-weight:700;font-size:18.5px;margin-bottom:14px;letter-spacing:.2px}
  .therapy-list{list-style:none}
  .therapy-list>li{position:relative;padding-left:16px;margin-bottom:7px}
  .therapy-list>li::before{content:"";position:absolute;left:2px;top:5px;width:6px;height:6px;border-radius:50%;background:#fff}
  .therapy-list b{font-weight:700}
  .therapy-list p{margin-top:3px}
  .tick-list{list-style:none;margin-top:3px}
  .tick-list li{padding-left:14px;position:relative}
  .tick-list li::before{content:"";position:absolute;left:2px;top:3px;width:4px;height:8px;border:solid #fff;border-width:0 2px 2px 0;transform:rotate(40deg)}
  .therapy-price{margin-top:14px;font-family:"Roboto Condensed",Arial,sans-serif;font-weight:700;font-size:20px}
  .therapy-price .num{font-size:34px}

  /* footer */
  .footer-curve{position:absolute;left:0;top:1010px;width:899px;height:190px}
  .massage{position:absolute;left:30px;top:1108px;width:520px;color:#fff}
  .massage h3{font-family:"Roboto",Arial,sans-serif;font-weight:700;font-size:16px;margin-bottom:12px}
  .massage ul{list-style:none;display:flex;gap:50px;font-size:13.5px}
  .massage li{position:relative;padding-left:16px}
  .massage li::before{content:"";position:absolute;left:0;top:5px;width:6px;height:6px;border-radius:50%;background:var(--pink)}
  .massage-photo{position:absolute;left:548px;top:1008px;width:360px;height:200px;border-top-left-radius:200px 150px;border-top:7px solid var(--pink);border-left:7px solid var(--pink);
    background:linear-gradient(160deg,#e2c6b2 0%,#b98f78 60%,#7e6253 100%)}
</style>
</head>
<body>
<main class="flyer">

  <div class="hero-photo" role="img" aria-label="Photo of a woman in a green bikini relaxing on a sunny beach"></div>

  <h1 class="brand-title">Velvet Dune</h1>
  <ul class="hero-points">
    <li>Non invasive and pain free</li>
    <li>Look amazing and feel confident with a Hair Free body</li>
    <li>1 treatment a month will ensure you are bikini hot for the summer months</li>
    <li>Part payments available</li>
  </ul>

  <svg class="hero-curve" viewBox="0 0 899 160" preserveAspectRatio="none" aria-hidden="true">
    <path d="M0,60 Q430,150 899,10 L899,48 Q430,178 0,96 Z" fill="var(--teal)"/>
    <path d="M0,96 Q430,178 899,48 L899,70 Q430,194 0,116 Z" fill="var(--pink)"/>
    <path d="M0,116 Q430,194 899,70 L899,160 L0,160 Z" fill="#fff"/>
  </svg>

  <div class="offer-badge">
    <svg viewBox="-86 -86 172 172" aria-hidden="true">
      <polygon fill="var(--teal)" stroke="#fff" stroke-width="3" points="80,0 64.7,12.9 73.9,30.6 54.8,36.7 56.6,56.6 36.7,54.8 30.6,73.9 12.9,64.7 0,80 -12.9,64.7 -30.6,73.9 -36.7,54.8 -56.6,56.6 -54.8,36.7 -73.9,30.6 -64.7,12.9 -80,0 -64.7,-12.9 -73.9,-30.6 -54.8,-36.7 -56.6,-56.6 -36.7,-54.8 -30.6,-73.9 -12.9,-64.7 0,-80 12.9,-64.7 30.6,-73.9 36.7,-54.8 56.6,-56.6 54.8,-36.7 73.9,-30.6 64.7,-12.9"/>
    </svg>
    <div class="offer-text">
      <span class="small">Take full</span>
      <span class="small">advantage of our</span>
      <span class="small">OPENING SPECIALS</span>
      <span class="big">30%-40%</span>
      <span class="small">savings</span>
    </div>
  </div>

  <div class="faint-portrait" role="img" aria-label="Faint close-up photo of a woman's eye"></div>

  <div class="intro">
    <p class="intro-lead">Now is the time to <span class="script">Start</span></p>
    <p class="intro-headline">Don't Delay</p>
  </div>

  <section class="cellulite">
    <h2 class="section-head">Cellulite &amp; Fat Reduction</h2>
    <p>Now you too can look amazing without invasive surgery, downtime or discomfort Lorna Pettigrew &amp; Beatrix Holloway are avid recipients of this treatment. Effective on all skin types and delivers fast measurable results for:</p>
    <ul class="dot-list">
      <li>Helping mums regain their pre-baby figures</li>
      <li>Losing the love handles (but keeping the love)</li>
      <li>Stretch mark reduction</li>
      <li>Skin tightening</li>
      <li>Cellulite busting on Arms, tummy, thighs.</li>
      <li>Man boob reduction.</li>
    </ul>
    <h3 class="sub-head">Latest technology</h3>
    <ul class="dot-list">
      <li>Bi Polar radio frequency (RF)</li>
      <li>Infrared light</li>
      <li>Negative pressure (Vacuum)</li>
      <li>Tissue manipulation through roller mechanical massage.</li>
    </ul>
  </section>

  <p class="call-out"><span class="num">50%</span> saving Call now</p>

  <section class="therapy-panel">
    <h2>PDT LED REJUVENATION LIGHT THERAPY</h2>
    <ul class="therapy-list">
      <li><b>KOTR Researchers found:</b>
        <p>Fibroblast and muscles grew 5 times faster, stimulates reconstruction of collagenous fibres of the dermis</p></li>
      <li><b>These findings and more assist with:</b>
        <ul class="tick-list">
          <li>Remove freckles, sunburn pigmentation,</li>
          <li>Cures acne and hair follicle inflammation</li>
          <li>Anti aging skin tightening</li>
          <li>Reduces pore size</li>
          <li>Improve the skin texture</li>
          <li>Improves circulation</li>
        </ul></li>
      <li><b>Red light:</b> reduces pore size, softens skin wrinkles, reduces acne</li>
      <li><b>Blue light:</b> Kills the acne bacillus to eliminate acne, inhibit inflammation</li>
      <li><b>Yellow light:</b> Skin tightening, whitening and softens skin wrinkles</li>
      <li><b>Purple light:</b> combination of red &amp; blue lights treats acne scars</li>
      <li>Orange light increases cell energy and accelerates metabolism</li>
    </ul>
    <p class="therapy-price"><span class="num">$55</span> Saving and relax under the lights</p>
  </section>

  <svg class="footer-curve" viewBox="0 0 899 190" preserveAspectRatio="none" aria-hidden="true">
    <path d="M0,30 Q300,70 560,40 L560,62 Q300,96 0,58 Z" fill="var(--pink)"/>
    <path d="M0,58 Q300,96 560,62 L560,190 L0,190 Z" fill="var(--teal)"/>
  </svg>

  <section class="massage">
    <h3>Who can resist a soothing Hot stone massage therapy after</h3>
    <ul>
      <li>A hard stressful day at work</li>
      <li>Aches and muscular pain</li>
    </ul>
  </section>

  <div class="massage-photo" role="img" aria-label="Photo of a woman relaxing during a hot stone massage with a white lily"></div>

</main>
</body>
</html>
```